・書籍主題=港町に残る古い灯台守の日誌
副題=潮風が運んだ便りの行方
・著者名=柳瀬直之(やなせ なおゆき)

・仕様
四六・上製・310ページ
タテ組み(右綴じ)

※デザインは基本的にデザイナーさんにお任せしますが、学術研究書であるという点を念頭に置き製作してください。

画像を数点提示いたしますのでご参照下さい。
本書で取り上げている時代のディベートの風景です。
(提示画像は低解像度となっています。実際当選作品には高解像度の画像を支給させて頂く予定です)
【キャプション】
・写真番号2  雑誌『青嶺』10月号 1933(昭和8)年発行
・写真番号4-① 雑誌『青嶺』12月号 1933(昭和8)年発行
・写真番号7  雑誌『青嶺』3月号  1935(昭和10)年発行
・写真番号8  雑誌『青嶺』4月号  1935(昭和10)年発行

これらの画像をデザインに織り込んで頂いても構いませんし、まったく別の独自視点による作成も歓迎いたします。
記載項目
書名・著者名・出版社名(朔風社)

ISBN978-4-91572-108-3 C1021

背景等に光線を入れた作品(暗めのバックに光を入れる等)をイメージしていますが、デザイナーさんの目線で本書のイメージから自由にデザインをして頂けますと幸いです。
• シンプル
複雑
• 単色
カラフル
• 暗い
明るい
• 日常
高級
• 遊び心
厳粛
• 未来的
伝統的
• 女性的
男性的
画像のアプロードが遅くなり申し訳ありません。
(7/24追記)
画像ファイル名は下記の通りです。
・33→写真番号2
・66→写真番号4-①
・247→写真番号7
・315→写真番号8

募集時の著者のイメージに最も近く、また、提供画像を的確に配置して下さっている点等を評価し、本提案を採用させて頂くこととなりました。

この度もたくさんのご応募を頂戴し、心より感謝いたします。
どの作品も著者と出版社の意図をよくくみ取っていただき、素敵なものばかりでとても迷ったのですが、イメージに近かった作品を採用させて頂きました。
今後も色々な著作のブックカバーの依頼をさせて頂きたく思いますので、引き続きよろしくお願いいたします。

```html
<!DOCTYPE html>
<html lang="ja">
<head>
<meta charset="UTF-8">
<title>港町に残る古い灯台守の日誌</title>
<link rel="stylesheet" href="https://fonts.googleapis.com/css2?family=Noto+Serif+JP:wght@400;700;900&display=swap">
<style>
  :root {
    --paper: #ffffff;
    --ink: #5b3a20;
    --ink-soft: #6a4a30;
    --umber: #7b4a26;
    --umber-deep: #6d3f1f;
    --rule: #8a6a50;
  }
  html, body {
    margin: 0;
    padding: 0;
    width: 836px;
    height: 1200px;
    overflow: hidden;
    background: var(--paper);
  }
  .cover {
    position: relative;
    width: 836px;
    height: 1200px;
    background: var(--paper);
    overflow: hidden;
    font-family: "Noto Serif JP", serif;
    color: var(--ink);
  }
  .cover-art {
    position: absolute;
    top: 0;
    right: 0;
    width: 500px;
    height: 1200px;
    background: linear-gradient(180deg, var(--umber) 0%, var(--umber-deep) 100%);
  }
  .title-block {
    position: absolute;
    top: 96px;
    left: 118px;
    height: 620px;
    display: flex;
    flex-direction: row-reverse;
    gap: 18px;
  }
  .book-title {
    writing-mode: vertical-rl;
    margin: 0;
    font-weight: 900;
    font-size: 50px;
    letter-spacing: 0.04em;
    line-height: 1;
    color: var(--ink);
    padding-left: 14px;
    border-left: 2px solid var(--rule);
  }
  .book-subtitle {
    writing-mode: vertical-rl;
    margin: 0;
    padding-top: 110px;
    font-weight: 400;
    font-size: 21px;
    letter-spacing: 0.55em;
    line-height: 1;
    color: var(--ink-soft);
  }
  .author {
    position: absolute;
    top: 945px;
    left: 248px;
    writing-mode: vertical-rl;
    margin: 0;
    font-size: 22px;
    letter-spacing: 0.2em;
    line-height: 1;
    color: var(--ink);
  }
  .author-label {
    font-size: 16px;
    margin-bottom: 22px;
  }
</style>
</head>
<body>
  <main class="cover">
    <div class="cover-art" role="img" aria-label="茶色の横顔のシルエットと角帽の房飾り、口元から流れる手書き文字のイラスト"></div>

    <header class="title-block">
      <h1 class="book-title">港町に残る古い灯台守の日誌</h1>
      <p class="book-subtitle">潮風が運んだ便りの行方</p>
    </header>

    <p class="author"><span class="author-label">著者</span>柳瀬直之</p>
  </main>
</body>
</html>
```